Redesign Application Page for Job Position

Would like to get a redesign on our Job Application Page.
You can use brennoxguard or valmoreta as references.

http://www.careersatklv.example/KLV/NCreateAccount.aspx?aga=qwtrzx4hemLK7

Target Market(s)

Professional Security Individuals

Industry/Entity Type

Security Guard

Coding

Coded - Design and coding required

Number of Pages Required

1 page

Font styles to use
Sans Serif

Colors
0255a3
3276b5
ffcf3e
fee18a

Requirements
Must have
• User Friendly, Easy Navigation. Must be very easy to read and understand what is required or missing.
Should not have
• Ugly or Bulky

```html
<!DOCTYPE html>
<html lang="en">
<head>
<meta charset="utf-8">
<title>Create an Application – Keldon Valley Guard Services</title>
<link rel="stylesheet" href="https://fonts.googleapis.com/css2?family=Oswald:wght@500;600;700&family=Roboto:wght@400;500;700;900&display=swap">
<style>
:root{
  --blue:#0255a3;
  --blue-mid:#3276b5;
  --yellow:#ffcf3e;
  --yellow-soft:#fee18a;
  --ink:#1d1d1d;
  --label:#555;
  --line:#c9c9c9;
  --red:#e02020;
  --cell-type:#b9cfe6;
  --footer:#1c1c1c;
}
*{box-sizing:border-box;margin:0;padding:0}
html,body{width:686px;height:1200px;overflow:hidden;background:#fff}
body{position:relative;font-family:"Roboto",Arial,sans-serif;color:var(--ink)}
.abs{position:absolute}
.hero{left:0;top:0;width:686px;height:190px;background:linear-gradient(90deg,#b9c7d3 0%,#dfe6ec 45%,#f1f3f5 100%)}
.brand{left:370px;top:40px;width:230px;text-align:center}
.brand-mark{width:44px;height:44px;border-radius:50%;background:var(--blue);margin:0 auto 18px}
.brand-name{font-family:"Oswald",Arial,sans-serif;font-weight:700;font-size:17px;color:var(--blue);white-space:nowrap;letter-spacing:-.2px}
.title-band{left:0;top:190px;width:686px;height:47px;background:var(--yellow);display:flex;align-items:center;justify-content:center}
.title-band h1{font-weight:900;font-size:21px;color:var(--ink);letter-spacing:-.2px}
.intro{left:0;top:263px;width:686px;text-align:center;font-size:10.5px}
.req{color:var(--red)}
.date-label{left:0;top:288px;width:686px;text-align:center;font-size:8px}
.date{left:0;top:305px;width:686px;text-align:center;font-family:"Oswald",Arial,sans-serif;font-weight:600;font-size:16px}
.lbl{font-size:7.5px;color:var(--label)}
.lbl .req{font-size:8px}
.field{height:16px;border:1px solid var(--line);background:#fff;font-size:5.6px;color:#999;padding:0 6px;display:flex;align-items:center}
.select::after{content:"";position:absolute;right:6px;top:6px;border:3px solid transparent;border-top:3.5px solid #777}
.radio{font-size:7.5px;color:var(--ink);display:flex;align-items:center;gap:4px}
.radio i{width:7px;height:7px;border-radius:50%;border:1px solid #bbb;display:inline-block;position:relative}
.radio i.on::after{content:"";position:absolute;left:1.5px;top:1.5px;width:3px;height:3px;border-radius:50%;background:var(--red)}
.section-title{left:0;width:686px;text-align:center;font-family:"Oswald",Arial,sans-serif;font-weight:600;font-size:18px;color:var(--ink)}
.license-band{left:0;top:597px;width:686px;height:220px;background:linear-gradient(180deg,var(--blue-mid) 0%,#2c6dac 100%)}
.th{height:24px;background:var(--yellow-soft);display:flex;align-items:center;justify-content:center;font-size:7.5px;font-weight:700}
.td-type{background:var(--cell-type);color:var(--blue);font-size:6.8px;padding:0 9px;display:flex;align-items:center;line-height:1.4}
.td-input{background:#fff}
.td-date{background:#fff;color:#bbb;font-size:7px;padding:0 10px;display:flex;align-items:center}
.cal{position:absolute;right:7px;top:50%;margin-top:-3.5px;width:7px;height:7px}
.avail-band{left:0;top:953px;width:686px;height:164px;background:linear-gradient(180deg,#fde28e 0%,var(--yellow-soft) 100%)}
.avail{left:92px;top:970px;width:500px;height:86px;border-collapse:collapse;background:rgba(255,236,170,.55)}
.avail th,.avail td{border:1px solid #f1cf6a;font-size:7.5px;font-weight:400;text-align:center;color:var(--ink)}
.avail th:first-child{width:79px}
.avail tr{height:21.5px}
.avail thead tr{height:21px}
.box{display:inline-block;width:8px;height:8px;border:1px solid #e6d39d;background:#fff6d6;border-radius:1px}
.btn{top:1070px;width:89px;height:25px;background:var(--blue);color:#fff;font-size:10.5px;font-weight:500;display:flex;align-items:center;justify-content:center}
.footer{left:0;top:1117px;width:686px;height:83px;background:var(--footer);text-align:center;color:#fff}
.footer h2{font-family:"Oswald",Arial,sans-serif;font-weight:500;font-size:13.5px;color:var(--yellow);margin-top:15px}
.footer .call{font-size:12px;margin-top:3px}
.footer .note{font-size:9.5px;margin-top:4px}
</style>
</head>
<body>

<div class="abs hero" role="img" aria-label="Photo of a uniformed security guard speaking into a radio in a bright office lobby"></div>
<div class="abs brand">
  <div class="brand-mark"></div>
  <div class="brand-name">KELDON VALLEY GUARD SERVICES, INC.</div>
</div>

<div class="abs title-band"><h1>CREATE AN APPLICATION</h1></div>

<p class="abs intro">Complete all required fields <span class="req">(colored red)</span>, then click "Continue" to create your account!</p>
<p class="abs date-label">Date Created:</p>
<p class="abs date">03-Jan-2018</p>

<!-- Row 1 -->
<span class="abs lbl" style="left:91px;top:347px">First Name: <span class="req">*</span></span>
<div class="abs field" style="left:91px;top:363px;width:157px"></div>
<span class="abs lbl" style="left:263px;top:347px">Middle Name:</span>
<div class="abs field" style="left:263px;top:363px;width:157px"></div>
<span class="abs lbl" style="left:435px;top:347px">Last Name:<span class="req">*</span></span>
<div class="abs field" style="left:435px;top:363px;width:157px"></div>

<!-- Row 2 -->
<span class="abs lbl" style="left:91px;top:396px">Gender :</span>
<span class="abs radio" style="left:91px;top:418px"><i></i>Male</span>
<span class="abs radio" style="left:130px;top:418px"><i class="on"></i>Female</span>
<span class="abs lbl" style="left:215px;top:396px">D.O.B :</span>
<div class="abs field select" style="left:215px;top:412px;width:62px">D/D...</div>
<div class="abs field select" style="left:286px;top:412px;width:63px">M/M...</div>
<div class="abs field select" style="left:358px;top:412px;width:62px">Y/Y...</div>
<span class="abs lbl" style="left:435px;top:396px">Street Address: <span class="req">*</span></span>
<div class="abs field" style="left:435px;top:412px;width:157px"></div>

<!-- Row 3 -->
<span class="abs lbl" style="left:91px;top:446px">City:</span>
<div class="abs field" style="left:91px;top:462px;width:157px"></div>
<span class="abs lbl" style="left:263px;top:446px">State:</span>
<div class="abs field select" style="left:263px;top:462px;width:157px"></div>
<span class="abs lbl" style="left:435px;top:446px">Nearest Office:</span>
<div class="abs field select" style="left:435px;top:462px;width:157px"></div>

<!-- Row 4 -->
<span class="abs lbl" style="left:91px;top:496px">Zip: <span class="req">*</span></span>
<div class="abs field" style="left:91px;top:512px;width:72px"></div>
<span class="abs lbl" style="left:173px;top:496px">Phone Number :</span>
<div class="abs field" style="left:173px;top:512px;width:75px">Cell...</div>
<div class="abs field" style="left:263px;top:512px;width:83px">Home...</div>
<span class="abs lbl" style="left:358px;top:496px">Job Position :</span>
<div class="abs field select" style="left:359px;top:512px;width:140px"></div>
<span class="abs lbl" style="left:512px;top:496px">SSN :<span class="req">*</span></span>
<div class="abs field" style="left:512px;top:512px;width:80px"></div>

<h2 class="abs section-title" style="top:553px">LICENSE DETAILS:</h2>

<div class="abs license-band" role="img" aria-label="Blue-tinted background photo of a security officer and a city skyline"></div>

<div class="abs th" style="left:91px;top:618px;width:178px">TYPE</div>
<div class="abs th" style="left:275px;top:618px;width:157px">NUMBER</div>
<div class="abs th" style="left:438px;top:618px;width:154px">EXPIRE DATE</div>

<div class="abs td-type" style="left:91px;top:647px;width:178px;height:19px">Guard Card</div>
<div class="abs td-input" style="left:275px;top:647px;width:157px;height:19px"></div>
<div class="abs td-date" style="left:438px;top:647px;width:154px;height:19px">01 / 19 / 2018<svg class="cal" viewBox="0 0 8 8"><rect x=".5" y="1.5" width="7" height="6" fill="none" stroke="#bbb"/><rect x=".5" y="1.5" width="7" height="2" fill="#bbb"/></svg></div>

<div class="abs td-type" style="left:91px;top:670px;width:178px;height:19px">Baton</div>
<div class="abs td-input" style="left:275px;top:670px;width:157px;height:19px"></div>
<div class="abs td-date" style="left:438px;top:670px;width:154px;height:19px">DD / MM / YYYY<svg class="cal" viewBox="0 0 8 8"><rect x=".5" y="1.5" width="7" height="6" fill="none" stroke="#bbb"/><rect x=".5" y="1.5" width="7" height="2" fill="#bbb"/></svg></div>

<div class="abs td-type" style="left:91px;top:694px;width:178px;height:18px">Gun Permit</div>
<div class="abs td-input" style="left:275px;top:694px;width:157px;height:18px"></div>
<div class="abs td-date" style="left:438px;top:694px;width:154px;height:18px">DD / MM / YYYY<svg class="cal" viewBox="0 0 8 8"><rect x=".5" y="1.5" width="7" height="6" fill="none" stroke="#bbb"/><rect x=".5" y="1.5" width="7" height="2" fill="#bbb"/></svg></div>

<div class="abs td-type" style="left:91px;top:717px;width:178px;height:18px">Transportation Workers Identification Card (TWIC)</div>
<div class="abs td-input" style="left:275px;top:717px;width:157px;height:18px"></div>
<div class="abs td-date" style="left:438px;top:717px;width:154px;height:18px">DD / MM / YYYY<svg class="cal" viewBox="0 0 8 8"><rect x=".5" y="1.5" width="7" height="6" fill="none" stroke="#bbb"/><rect x=".5" y="1.5" width="7" height="2" fill="#bbb"/></svg></div>

<div class="abs td-type" style="left:91px;top:740px;width:178px;height:18px">Merchant Mariner Credential (MMC)</div>
<div class="abs td-input" style="left:275px;top:740px;width:157px;height:18px"></div>
<div class="abs td-date" style="left:438px;top:740px;width:154px;height:18px">DD / MM / YYYY<svg class="cal" viewBox="0 0 8 8"><rect x=".5" y="1.5" width="7" height="6" fill="none" stroke="#bbb"/><rect x=".5" y="1.5" width="7" height="2" fill="#bbb"/></svg></div>

<div class="abs td-type" style="left:91px;top:763px;width:178px;height:30px">Standards of Training, Certification and<br>Watchkeeping for Seafarers (SCTW)</div>
<div class="abs td-input" style="left:276px;top:763px;width:156px;height:30px"></div>
<div class="abs td-date" style="left:439px;top:763px;width:153px;height:30px">DD / MM / YYYY<svg class="cal" viewBox="0 0 8 8"><rect x=".5" y="1.5" width="7" height="6" fill="none" stroke="#bbb"/><rect x=".5" y="1.5" width="7" height="2" fill="#bbb"/></svg></div>

<!-- Extra details -->
<span class="abs lbl" style="left:91px;top:850px">ID Document Type :</span>
<div class="abs field select" style="left:91px;top:866px;width:116px">Select...</div>
<span class="abs lbl" style="left:220px;top:850px">Additional Languages :</span>
<div class="abs field select" style="left:220px;top:866px;width:115px">Select...</div>
<span class="abs lbl" style="left:348px;top:850px">Email : <span class="req">*</span></span>
<div class="abs field" style="left:348px;top:866px;width:116px"></div>
<span class="abs lbl" style="left:477px;top:850px">How did you hear about us?</span>
<div class="abs field select" style="left:477px;top:866px;width:115px">Select...</div>

<h2 class="abs section-title" style="top:909px">WORK AVAILABILITY</h2>

<div class="abs avail-band" role="img" aria-label="Yellow-tinted background photo of a security officer"></div>

<table class="abs avail">
  <thead>
    <tr><th>Shift</th><th>Sun</th><th>Mon</th><th>Tue</th><th>Wed</th><th>Thu</th><th>Fri</th><th>Sat</th></tr>
  </thead>
  <tbody>
    <tr><td>Day Shift</td><td><i class="box"></i></td><td><i class="box"></i></td><td><i class="box"></i></td><td><i class="box"></i></td><td><i class="box"></i></td><td><i class="box"></i></td><td><i class="box"></i></td></tr>
    <tr><td>Swing Shift</td><td><i class="box"></i></td><td><i class="box"></i></td><td><i class="box"></i></td><td><i class="box"></i></td><td><i class="box"></i></td><td><i class="box"></i></td><td><i class="box"></i></td></tr>
    <tr><td>Night Shift</td><td><i class="box"></i></td><td><i class="box"></i></td><td><i class="box"></i></td><td><i class="box"></i></td><td><i class="box"></i></td><td><i class="box"></i></td><td><i class="box"></i></td></tr>
  </tbody>
</table>

<div class="abs btn" style="left:242px">CONTINUE</div>
<div class="abs btn" style="left:341px">DISCARD</div>

<footer class="abs footer">
  <h2>Need Help?</h2>
  <p class="call">Call Us at: (555) 014-2870</p>
  <p class="note">and ask for a Human Resource representative.</p>
</footer>

</body>
</html>
```